Business Card Design

Professional solutions in (servers, security, networks, programming)

Industry/Entity Type

Business

Contact Information for Business Card

Tarek Hounayni
Internet services and network solutions
DPV - RTLK - RTLB
netcare@qo-lam.com / 05917406238
www.qo-lam.com

```html
<!DOCTYPE html>
<html lang="en">
<head>
<meta charset="utf-8">
<title>Tarek Hounayni – Business Card</title>
<link rel="stylesheet" href="https://fonts.googleapis.com/css2?family=Montserrat:wght@500;600&display=swap">
<style>
  :root {
    --ink-black: #0b0b0b;
    --tile-dark: #161616;
    --tile-mid: #242424;
    --band-grey: #a6a6a6;
    --text-white: #ffffff;
    --icon-black: #111111;
  }
  html, body {
    margin: 0;
    padding: 0;
    width: 1200px;
    height: 668px;
    overflow: hidden;
    background: var(--ink-black);
  }
  .card {
    position: relative;
    width: 1200px;
    height: 668px;
    overflow: hidden;
    font-family: "Montserrat", Arial, sans-serif;
    color: var(--text-white);
  }
  .card__texture {
    position: absolute;
    inset: 0;
    background:
      radial-gradient(ellipse at 30% 20%, var(--tile-mid) 0%, transparent 60%),
      radial-gradient(ellipse at 80% 85%, var(--tile-dark) 0%, transparent 55%),
      linear-gradient(135deg, var(--tile-dark) 0%, var(--ink-black) 55%, var(--tile-dark) 100%);
  }
  .headline {
    position: absolute;
    top: 135px;
    left: 0;
    right: 0;
    height: 60px;
    display: flex;
    align-items: center;
  }
  .band {
    height: 60px;
    background: var(--band-grey);
  }
  .band--left { width: 60px; flex: none; }
  .band--right { flex: 1; }
  .headline__name {
    margin: 0 24px 0 22px;
    font-size: 60px;
    font-weight: 600;
    line-height: 60px;
    white-space: nowrap;
    text-transform: uppercase;
  }
  .identity {
    position: absolute;
    left: 82px;
    top: 198px;
  }
  .identity__role {
    margin: 0;
    font-size: 22px;
    font-weight: 500;
    line-height: 28px;
    text-transform: uppercase;
  }
  .identity__credentials {
    margin: 2px 0 0;
    font-size: 20px;
    font-weight: 500;
    line-height: 26px;
    text-transform: uppercase;
    word-spacing: 20px;
  }
  .contact {
    position: absolute;
    left: 724px;
    display: flex;
    align-items: center;
  }
  .contact__icon {
    width: 66px;
    height: 66px;
    flex: none;
  }
  .contact__text {
    font-weight: 500;
    text-transform: uppercase;
    white-space: nowrap;
  }
  .contact--email { top: 264px; }
  .contact--email .contact__text { margin-left: 44px; font-size: 20px; }
  .contact--phone { top: 411px; }
  .contact--phone .contact__text { margin-left: 38px; font-size: 31px; letter-spacing: 0.5px; }
  .contact--web { top: 562px; }
  .contact--web .contact__text { margin-left: 38px; font-size: 21px; }
</style>
</head>
<body>
<main class="card">
  <div class="card__texture" role="img" aria-label="Dark geometric triangle tile background"></div>

  <header class="headline">
    <div class="band band--left"></div>
    <h1 class="headline__name">Tarek Hounayni</h1>
    <div class="band band--right"></div>
  </header>

  <section class="identity">
    <p class="identity__role">Internet Services and Network Solutions</p>
    <p class="identity__credentials">DPV RTLK RTLB</p>
  </section>

  <div class="contact contact--email">
    <svg class="contact__icon" viewBox="0 0 66 66" aria-hidden="true">
      <circle cx="33" cy="33" r="33" fill="var(--text-white)"/>
      <rect x="17" y="22" width="32" height="22" fill="none" stroke="var(--icon-black)" stroke-width="2.5"/>
      <polyline points="17,22 33,36 49,22" fill="none" stroke="var(--icon-black)" stroke-width="2.5"/>
      <line x1="17" y1="44" x2="28" y2="32" stroke="var(--icon-black)" stroke-width="2"/>
      <line x1="49" y1="44" x2="38" y2="32" stroke="var(--icon-black)" stroke-width="2"/>
    </svg>
    <span class="contact__text">netcare@qo-lam.com</span>
  </div>

  <div class="contact contact--phone">
    <svg class="contact__icon" viewBox="0 0 66 66" aria-hidden="true">
      <circle cx="33" cy="33" r="33" fill="var(--text-white)"/>
      <path d="M22 18 l6 -2 l5 10 l-4 3 c2 5 5 8 10 10 l3 -4 l10 5 l-2 6 c-1 3 -4 4 -7 3 c-11 -4 -19 -12 -23 -23 c-1 -3 0 -6 2 -8 z" fill="var(--icon-black)"/>
    </svg>
    <span class="contact__text">05917406238</span>
  </div>

  <div class="contact contact--web">
    <svg class="contact__icon" viewBox="0 0 66 66" aria-hidden="true">
      <circle cx="33" cy="33" r="33" fill="var(--text-white)"/>
      <circle cx="33" cy="33" r="16" fill="var(--icon-black)"/>
      <path d="M24 24 c4 -2 7 0 8 3 c1 3 -2 4 -1 7 c1 3 -3 5 -5 3 c-2 -2 -4 -3 -5 -6 c0 -3 1 -5 3 -7 z" fill="var(--text-white)"/>
      <path d="M37 19 c3 1 6 3 8 6 c-2 1 -4 0 -5 2 c-1 2 2 3 1 5 c-2 1 -3 -1 -5 -2 c-1 -3 0 -5 1 -7 z" fill="var(--text-white)"/>
      <path d="M37 38 c3 -1 6 0 7 2 c-1 3 -4 6 -7 7 c-1 -3 -2 -6 0 -9 z" fill="var(--text-white)"/>
    </svg>
    <span class="contact__text">www.qo-lam.com</span>
  </div>
</main>
</body>
</html>
```